Menubook for a 2star restaurant

Hey,
We are looking for a new menu for a 2 star restaurant in Belgium. They want a clean, abstract, with small light accents of gold, copper. The format will be 21 cm by 21 cm. and the booklet will have 4 printable sides inc front & back. Only the logo on the front. The wine list will be separate so it should not be included in the design. "Bites" - "voorgerechten" - "hoofdgerechten" & "nagerechten" must be copied.

Industry/Entity Type

Restaurant

Requirements
Must have
• Clean look
Nice to have
• touches of gold

```html
<!DOCTYPE html>
<html lang="nl">
<head>
<meta charset="utf-8">
<title>saffra — menukaart</title>
<link rel="stylesheet" href="https://fonts.googleapis.com/css2?family=Montserrat:wght@300;400;700&display=swap">
<style>
  :root {
    --bg: #d9d9d9;
    --paper: #f7f7f5;
    --ink: #1b1a18;
    --text: #4a4a48;
    --gold: #e9b22c;
    --gold-light: #f4cd57;
    --copper: #e5a11f;
    --fold: rgba(0,0,0,0.08);
  }
  * { box-sizing: border-box; margin: 0; padding: 0; }
  html, body { width: 1200px; height: 960px; overflow: hidden; }
  body {
    background: var(--bg);
    font-family: "Montserrat", sans-serif;
    color: var(--text);
    position: relative;
  }
  .spread {
    position: absolute;
    left: 160px;
    width: 880px;
    height: 440px;
    display: flex;
    box-shadow: 0 6px 18px rgba(0,0,0,0.18);
  }
  .spread--inside { top: 20px; }
  .spread--cover { top: 500px; }
  .page {
    position: relative;
    width: 440px;
    height: 440px;
    background: var(--paper);
    overflow: hidden;
  }
  .page + .page { border-left: 1px solid var(--fold); }

  /* decorative edges */
  .brush-edge { position: absolute; background: var(--ink); }
  .brush-edge--left { left: 0; top: 20px; width: 26px; height: 400px; }
  .brush-edge--right { right: 0; top: 0; width: 26px; height: 150px; }
  .brush-edge--cover-left { left: 0; top: 0; width: 22px; height: 440px; }
  .brush-edge--cover-right { right: 0; top: 60px; width: 24px; height: 380px; }
  .gold-splatter {
    position: absolute;
    background: radial-gradient(circle, rgba(229,161,31,0.55) 0%, rgba(229,161,31,0.25) 45%, rgba(229,161,31,0) 72%);
  }
  .gold-splatter--bottom-left { left: 10px; top: 300px; width: 150px; height: 140px; }
  .gold-splatter--top-right { right: 20px; top: 0; width: 130px; height: 100px; }

  /* headings */
  .section-title {
    display: inline-block;
    background: linear-gradient(90deg, var(--copper), var(--gold-light) 50%, var(--gold));
    color: var(--ink);
    font-weight: 700;
    font-size: 12px;
    letter-spacing: 0.04em;
    text-transform: uppercase;
    padding: 6px 26px;
    margin-bottom: 10px;
  }
  .menu-section {
    position: absolute;
    text-align: center;
  }
  .menu-list { list-style: none; }
  .menu-item { font-weight: 300; font-size: 10.5px; line-height: 1.35; color: var(--text); }
  .menu-item .price { color: var(--copper); font-weight: 400; margin-left: 3px; }
  .menu-detail { font-weight: 700; font-size: 7.5px; line-height: 1.4; color: var(--ink); margin-bottom: 5px; }
  .menu-group { margin-bottom: 6px; }
  .menu-note { font-weight: 300; font-size: 10.5px; line-height: 1.35; }

  .section--aperitivi { left: 40px; top: 60px; width: 180px; }
  .section--bites { left: 215px; top: 40px; width: 210px; }
  .section--voorgerechten { left: 100px; top: 270px; width: 300px; }
  .section--hoofdgerechten { left: 40px; top: 34px; width: 360px; }
  .section--nagerechten { left: 40px; top: 318px; width: 360px; }

  /* cover */
  .gold-wash {
    position: absolute;
    background: linear-gradient(135deg, var(--gold-light) 0%, var(--gold) 50%, var(--copper) 100%);
    opacity: 0.92;
  }
  .gold-wash--back { left: 150px; top: 0; width: 290px; height: 300px; border-radius: 0 0 0 60%; }
  .gold-wash--front { left: 0; top: 40px; width: 380px; height: 400px; border-radius: 0 50% 0 0; }
  .ink-block {
    position: absolute;
    left: 130px; top: 140px;
    width: 200px; height: 190px;
    background: var(--ink);
    border-radius: 10px;
    display: flex; align-items: center; justify-content: center;
  }
  .wordmark {
    font-family: "Montserrat", sans-serif;
    font-weight: 300;
    letter-spacing: 0.45em;
    font-size: 18px;
  }
  .wordmark--back { position: absolute; left: 95px; top: 340px; color: var(--ink); }
  .wordmark--front { color: var(--gold); }
</style>
</head>
<body>

<section class="spread spread--inside" aria-label="Binnenzijde menukaart">
  <article class="page page--left">
    <div class="brush-edge brush-edge--left" role="img" aria-label="Zwarte penseelstreek langs de rand"></div>
    <div class="gold-splatter gold-splatter--bottom-left" role="img" aria-label="Gouden spatten"></div>

    <div class="menu-section section--aperitivi">
      <h2 class="section-title">Aperitivi</h2>
      <ul class="menu-list">
        <li class="menu-item">Ca' del Pino<span class="price">19</span></li>
        <li class="menu-item menu-group">Maison Verlaine<span class="price">21</span></li>
        <li class="menu-item">Arancio Spritz<span class="price">15</span></li>
        <li class="menu-item menu-group">Hugo<span class="price">15</span></li>
        <li class="menu-item">Gin Marino<span class="price">18</span></li>
        <li class="menu-item">Copperleaf<span class="price">19</span></li>
        <li class="menu-item menu-group">Nulla Gin (Non Alcoholisch)<span class="price">19</span></li>
        <li class="menu-item">Negroni Sbagliato<span class="price">17</span></li>
        <li class="menu-item">Classic Negroni<span class="price">19</span></li>
        <li class="menu-item">Amaretto Sunrise<span class="price">15</span></li>
      </ul>
    </div>

    <div class="menu-section section--bites">
      <h2 class="section-title">Bites</h2>
      <ul class="menu-list">
        <li class="menu-item">Oester Marennes (1St)<span class="price">9</span></li>
        <li class="menu-detail">Jalapeño | Komkommer | Ajo Blanco<br>Supplement Kaviaar 5Gr (+ €18)</li>
        <li class="menu-item menu-group">'Nduja Risotto Croquettes (2St)<span class="price">9</span></li>
        <li class="menu-item">Charcuterie<span class="price">15</span></li>
        <li class="menu-detail">Cornichon | Olijven</li>
        <li class="menu-item">Koude Amandel-Knoflook Zuppa<span class="price">14</span></li>
        <li class="menu-detail">Fregola | Kreeft</li>
      </ul>
    </div>

    <div class="menu-section section--voorgerechten">
      <h2 class="section-title">Voorgerechten</h2>
      <ul class="menu-list">
        <li class="menu-item menu-group">Antipasti *<span class="price">35 p.p.</span></li>
        <li class="menu-item">Pizzetta Amaro</li>
        <li class="menu-detail">Met 1/2 Kreeft | Doperwt | Basilicum | Courgette <span class="price">37</span><br>Ook Vegetarisch Te Bestellen <span class="price">32</span></li>
      </ul>
    </div>
  </article>

  <article class="page page--right">
    <div class="brush-edge brush-edge--right" role="img" aria-label="Zwarte penseelstreek in de hoek"></div>
    <div class="gold-splatter gold-splatter--top-right" role="img" aria-label="Gouden spatten"></div>

    <div class="menu-section section--hoofdgerechten">
      <h2 class="section-title">Hoofdgerechten</h2>
      <ul class="menu-list">
        <li class="menu-item">Spaghetti Vongole *<span class="price">29</span></li>
        <li class="menu-detail">Bosui | Piemento | Zilte Groenten</li>
        <li class="menu-item">Kabeljauw Rug *<span class="price">36</span></li>
        <li class="menu-detail">Limoen | Kappertjes | Mosselen | Safraan</li>
        <li class="menu-item">Kalfsfilet *<span class="price">46</span></li>
        <li class="menu-detail">Paarse Bloemkool | Girolle | Groen Asperge | Daslook | Pijpajuin</li>
        <li class="menu-item">Insalate Del Giorno</li>
        <li class="menu-detail">Vlees of Vis <span class="price">40</span><br>Veggie <span class="price">33</span></li>
        <li class="menu-item">Gnocchi<span class="price">29</span></li>
        <li class="menu-detail">Salie | Spinazie | Borlotto</li>
        <li class="menu-item">Gepocheerd Hoeve Ei<span class="price">36</span></li>
        <li class="menu-detail">Girolle | Daslook | Groene Asperges</li>
      </ul>
    </div>

    <div class="menu-section section--nagerechten">
      <h2 class="section-title">Nagerechten</h2>
      <ul class="menu-list">
        <li class="menu-item">Assortiment Van 5 Italiaanse Kazen<span class="price">27</span></li>
        <li class="menu-item">Amalfi Citroen Met Meringue *<span class="price">16</span></li>
        <li class="menu-note">* Menu | 5 Gangen<span class="price">95</span></li>
      </ul>
    </div>
  </article>
</section>

<section class="spread spread--cover" aria-label="Voor- en achterzijde menukaart">
  <article class="page page--back">
    <div class="brush-edge brush-edge--cover-left" role="img" aria-label="Zwarte penseelstreek langs de rand"></div>
    <div class="gold-wash gold-wash--back" role="img" aria-label="Gouden penseelvlak"></div>
    <p class="wordmark wordmark--back">saffra</p>
  </article>

  <article class="page page--front">
    <div class="gold-wash gold-wash--front" role="img" aria-label="Groot gouden penseelvlak"></div>
    <div class="brush-edge brush-edge--cover-right" role="img" aria-label="Zwarte penseelstreek langs de rand"></div>
    <div class="ink-block" role="img" aria-label="Zwarte inktstreken met de naam van het restaurant">
      <p class="wordmark wordmark--front">saffra</p>
    </div>
  </article>
</section>

</body>
</html>
```